Marlow Hire Business Card for recruitment company

We are looking for a Business Card Design that incorporates our personal details and our busines name and logo. We are a specialized search consultancy that recruit Property and Construction professionals.
We would like a business card that stands out and is appealing to the Construction and Property industry as well.

Target Market(s)

people in the construction and property industry

Contact Information for Business Card

Business Name and logo

Font styles to use
Serif

Colors
0094D4
00A9DD
6FCCEA
C7EBF8
E9F6FB

Requirements
Must have
• Business name and logo as well as contact details
Should not have
• No photos of us please

```html
<!DOCTYPE html>
<html lang="en">
<head>
<meta charset="utf-8">
<title>Marlow Hire – Business Card</title>
<link href="https://fonts.googleapis.com/css2?family=Josefin+Sans:wght@300;400;600&display=swap" rel="stylesheet">
<style>
  :root {
    --ink: #034a63;
    --ink-deep: #023d53;
    --paper: #f1f1f1;
    --paper-shade: #e6e6e6;
    --backdrop: #a4a4a4;
    --white: #ffffff;
  }
  * { box-sizing: border-box; margin: 0; padding: 0; }
  html, body {
    width: 1200px; height: 1005px; overflow: hidden;
    background: var(--backdrop);
    font-family: "Josefin Sans", "Futura", sans-serif;
  }
  .stage { position: relative; width: 1200px; height: 1005px; }
  .card {
    position: absolute; left: 292px; width: 616px; height: 352px;
    overflow: hidden;
  }
  /* Front */
  .card-front { top: 128px; background: var(--ink); }
  .front-wordmark {
    position: absolute; inset: 0;
    display: flex; align-items: center; justify-content: center;
    color: var(--white); font-weight: 300; font-size: 56px;
    letter-spacing: 3px; padding-top: 6px;
  }
  /* Back */
  .card-back {
    top: 524px;
    background: linear-gradient(135deg, var(--paper) 40%, var(--paper-shade) 100%);
    color: var(--ink);
  }
  .person { position: absolute; left: 33px; top: 24px; }
  .person-name { font-size: 34px; font-weight: 600; letter-spacing: 0.5px; line-height: 1; }
  .person-role { font-size: 16px; font-weight: 400; letter-spacing: 0.5px; margin-top: 4px; }
  .contact-list { position: absolute; left: 33px; top: 170px; list-style: none; }
  .contact-item {
    display: flex; align-items: center; height: 22px;
    font-size: 15px; font-weight: 600; letter-spacing: 0.3px;
  }
  .contact-item + .contact-item { margin-top: 22px; }
  .contact-icon { width: 26px; height: 22px; margin-right: 25px; flex: none; }
  .tower {
    position: absolute; left: 463px; top: 0; width: 83px; height: 247px;
    background: var(--ink);
  }
  .tower-base {
    position: absolute; left: 463px; top: 294px; width: 83px; height: 58px;
    background: var(--ink);
  }
  .back-wordmark {
    position: absolute; left: 402px; top: 258px; width: 192px;
    text-align: center; font-size: 25px; font-weight: 300;
    letter-spacing: 0.5px; white-space: nowrap;
  }
</style>
</head>
<body>
<main class="stage">
  <section class="card card-front">
    <div class="front-wordmark">MARLOW HIRE</div>
  </section>

  <section class="card card-back">
    <div class="person">
      <h1 class="person-name">OWEN FIELDING</h1>
      <p class="person-role">SENIOR CONSULTANT</p>
    </div>

    <ul class="contact-list">
      <li class="contact-item">
        <svg class="contact-icon" viewBox="0 0 26 22" aria-hidden="true">
          <path d="M5 2 L9 2 L11 7 L8.5 9 Q11 14 15 16 L17 13.5 L22 15.5 L22 19.5 Q21 21 18.5 21 Q9 20 4 10 Q3 5 5 2 Z" fill="var(--ink)"/>
        </svg>
        <span>+64 27 480 2291</span>
      </li>
      <li class="contact-item">
        <svg class="contact-icon" viewBox="0 0 26 22" aria-hidden="true">
          <rect x="1" y="3" width="24" height="16" fill="none" stroke="var(--ink)" stroke-width="1.4"/>
          <path d="M1 3 L13 13 L25 3 M1 19 L10 10.5 M25 19 L16 10.5" fill="none" stroke="var(--ink)" stroke-width="1.4"/>
        </svg>
        <span>AVA@MARLOWHIRE.NZ</span>
      </li>
      <li class="contact-item">
        <svg class="contact-icon" viewBox="0 0 26 22" aria-hidden="true">
          <g fill="none" stroke="var(--ink)" stroke-width="1.4">
            <circle cx="13" cy="11" r="10"/>
            <ellipse cx="13" cy="11" rx="4.5" ry="10"/>
            <path d="M13 1 V21 M3 11 H23 M5 5.5 H21 M5 16.5 H21"/>
          </g>
        </svg>
        <span>WWW.MARLOWHIRE.NZ</span>
      </li>
    </ul>

    <div class="tower" role="img" aria-label="Building graphic: tall block with window grid"></div>
    <div class="back-wordmark">MARLOW HIRE</div>
    <div class="tower-base" role="img" aria-label="Building graphic: base with doorway"></div>
  </section>
</main>
</body>
</html>
```